南谷 睦月というペンネームで活動しているものです。

本業は組織・人財開発領域に特化した支援を行う会社において、
企画の提案、プロジェクトマネジメント、依頼後の進捗管理など、
お客様の中に自身も入りながら、経営を変えていくような支援を行っています。

ご依頼をさせていただく表紙デザインですが、
9月16日にPagoraにて、下記の内容を発行いたしました。
============================
現場を変える人が大切にする4つの視点:
~挑戦した人々の物語から静かに学び取る~

www.bookvale-store.jp/item/Q72KD4MX3N
こちらの内容について、発行に向けた表紙手配が間に合わなかったこともあり、
一旦はデザインを自身で考え、発行をいたしましたが、
表紙は書籍の顔ということもあり、作成依頼を進めることに決めました。

デザイン制作にあたって検討いただきたいのは下記2点です。

検討に当たってのポイントは下記2点です。
① 悩みに対しての答えが見つかるような印象を持てる
② あまり複雑すぎないデザインであること

① 悩みに対しての答えが見つかるような印象を持てる
・取り上げたPagoraでは、スキル・ノウハウ本ではなく、
実践されている方が直面されたエピソードをもとにして、
悩みを解決するためのヒントを取り上げています。
そのようなニュアンスが感じられるようなデザインに期待です。

② あまり複雑なデザインではないこと
・凝ったデザインよりは、わかりやすいデザインを好む方です。
複雑なカラーよりは、色を限りながらも、与えられた題材に対しての
表現を頂けるようなデザインが好みではあります。
※ が、良いものが出てくれば、それ限りではございませんので、
あくまで、現時点の好みとしてお伝えを致します

最終的に今回のコンペでは「R_hoshidaさん」のデザインを採用させて頂きます。
重視した点は改めて、下記の2点がベースとなります。
① 悩みに対しての答えが見つかるような印象を持てる
② あまり複雑なデザインではないこと
絵で①のイメージを喚起しつつ、今回の書籍で押し出していることを文字で強調いただく構成となっており、②の点からも適切と考えて採択をさせて頂きました。

改めて、この度はご提案をいただきましてありがとうございます。

引き続き、個人的な目標としては3か月~6か月に1回の頻度で、
Pagora向けの発行物を執筆していく予定です。
また、このような形でご支援の相談をさせていただきますので、
よろしければ是非、お力添えをどうぞお願い申し上げます。

```html
<!DOCTYPE html>
<html lang="ja">
<head>
<meta charset="UTF-8">
<title>現場を変える人が大切にする4つの視点</title>
<link rel="stylesheet" href="https://fonts.googleapis.com/css2?family=Noto+Sans+JP:wght@900&family=Noto+Serif+JP:wght@600;700&display=swap">
<style>
  :root {
    --title-green: #3b8c2f;
    --accent-lime: #a9c71e;
    --ink: #2a2a2a;
    --paper: #ffffff;
    --chart-line: #e4e4e4;
    --hero-glow: #fbfff0;
    --hero-light: #8fd03e;
    --hero-mid: #5aa82c;
    --hero-dark: #1f4f14;
  }
  html, body {
    margin: 0;
    padding: 0;
    overflow: hidden;
    background: var(--paper);
  }
  .cover {
    position: relative;
    width: 750px;
    height: 1200px;
    overflow: hidden;
    background: var(--paper);
  }
  .hero {
    position: absolute;
    left: 0;
    top: 0;
    width: 750px;
    height: 475px;
    background:
      radial-gradient(circle at 150px 265px, var(--hero-glow) 0%, rgba(240,255,200,0.85) 7%, rgba(190,235,110,0.45) 18%, rgba(143,208,62,0) 34%),
      linear-gradient(180deg, rgba(20,50,10,0.35) 0%, rgba(20,50,10,0) 30%, rgba(20,50,10,0) 75%, rgba(20,50,10,0.3) 100%),
      radial-gradient(ellipse 75% 90% at 22% 45%, var(--hero-light) 0%, var(--hero-mid) 50%, var(--hero-dark) 100%);
  }
  .chart {
    position: absolute;
    left: 0;
    top: 475px;
    width: 750px;
    height: 725px;
  }
  .title-line {
    position: absolute;
    left: 20px;
    margin: 0;
    font-family: "Noto Sans JP", sans-serif;
    font-weight: 900;
    font-size: 95px;
    line-height: 1;
    color: var(--title-green);
    white-space: nowrap;
  }
  .line-1 { top: 500px; }
  .line-2 { top: 602px; }
  .line-3 { top: 706px; }
  .line-4 { top: 815px; font-size: 92px; }
  .line-4 .count {
    font-size: 140px;
    color: var(--accent-lime);
    vertical-align: -8px;
    margin-right: 4px;
  }
  .author {
    position: absolute;
    right: 35px;
    top: 505px;
    text-align: right;
    font-family: "Noto Serif JP", serif;
    color: var(--ink);
  }
  .author-name {
    font-size: 46px;
    font-weight: 700;
    letter-spacing: 6px;
    line-height: 1.1;
  }
  .author-roman {
    font-size: 25px;
    font-style: italic;
    font-weight: 600;
    margin-top: 6px;
  }
  .subtitle {
    position: absolute;
    right: 22px;
    top: 985px;
    text-align: right;
    font-family: "Noto Serif JP", serif;
    font-weight: 600;
    font-size: 38px;
    line-height: 1.65;
    color: var(--ink);
    margin: 0;
  }
</style>
</head>
<body>
  <main class="cover">
    <div class="hero" role="img" aria-label="緑の背景に吊り下げられた電球が横一列に並び、左端の一つだけが明るく灯っている写真"></div>

    <svg class="chart" viewBox="0 0 750 725" aria-hidden="true">
      <g fill="none" stroke="var(--chart-line)" stroke-width="3">
        <polygon points="500,170 714,325 632,577 368,577 286,325"/>
        <polygon points="500,260 628,353 579,504 421,504 372,353"/>
        <line x1="500" y1="395" x2="500" y2="170"/>
        <line x1="500" y1="395" x2="714" y2="325"/>
        <line x1="500" y1="395" x2="632" y2="577"/>
        <line x1="500" y1="395" x2="368" y2="577"/>
        <line x1="500" y1="395" x2="286" y2="325"/>
      </g>
    </svg>

    <h1>
      <span class="title-line line-1">現場を</span>
      <span class="title-line line-2">変える人が</span>
      <span class="title-line line-3">大切にする</span>
      <span class="title-line line-4"><span class="count">4</span>つの視点</span>
    </h1>

    <div class="author">
      <div class="author-name">南谷 睦月</div>
      <div class="author-roman">Minamitani Mutsuki</div>
    </div>

    <p class="subtitle">挑戦した人々の物語から<br>静かに学び取る</p>
  </main>
</body>
</html>
```